JoyCrates Brochure

We need to create a brochure to go inside the gift pack for a new gift experiences company, JoyCrates. The brochure - which accompanies the gift certificate & info about the chosen experience - will provide information about our company itself. The brochure will need to be half US letter size.

The winner of this contest will be asked to design the rest of the contents of the gift pack.

To assist with this project, please find:
- brochure text/instructions
- company logo (preview and zipped file with assets)
-sample images
-visual showing gift pack to indicate size.

```html
<!DOCTYPE html>
<html lang="en">
<head>
<meta charset="utf-8">
<title>JoyCrates Brochure – Our Experiences</title>
<link href="https://fonts.googleapis.com/css2?family=Poppins:wght@200;300;400;600;700&family=Great+Vibes&display=swap" rel="stylesheet">
<style>
  :root{
    --red:#e3262d;
    --ink:#1d1d1d;
    --white:#ffffff;
    --paper:#ffffff;
    --grey-band:rgba(225,225,225,0.88);
  }
  *{box-sizing:border-box;margin:0;padding:0}
  html,body{width:1200px;height:388px;overflow:hidden;background:var(--paper)}
  .spread{position:relative;width:1200px;height:388px;overflow:hidden;font-family:"Poppins",sans-serif;color:var(--ink);background:var(--paper)}

  .photo{position:absolute}
  .photo-cooking{left:0;top:0;width:330px;height:388px;
    background:linear-gradient(90deg,#b9aa92 0%,#cfc3b0 35%,#e7e2da 65%,rgba(255,255,255,0) 100%)}
  .photo-cooking::after{content:"";position:absolute;inset:0;
    background:linear-gradient(180deg,rgba(255,255,255,0) 55%,rgba(255,255,255,0.75) 100%)}
  .photo-car{left:560px;top:0;width:640px;height:388px;
    background:linear-gradient(90deg,rgba(255,255,255,0) 0%,#dcdcdc 28%,#b0b0b0 40%,#c3151c 52%,#d52a2f 75%,#b8121a 100%)}

  .circle{position:absolute;border-radius:50%;border:3px solid var(--white);box-shadow:0 1px 4px rgba(0,0,0,.12)}
  .circle-spa{left:258px;top:244px;width:152px;height:152px;background:radial-gradient(circle at 60% 45%,#e2b79c,#7a4f3a 80%)}
  .circle-sky{left:622px;top:-12px;width:110px;height:110px;background:linear-gradient(160deg,#3d8fd8,#a9d3f2)}
  .circle-kayak{left:689px;top:18px;width:155px;height:155px;background:radial-gradient(circle at 55% 50%,#3f9da0,#1e5f6a 85%)}

  .ribbon{position:absolute;top:0;width:81px;height:52px;background:var(--red);
    color:var(--white);font-family:"Great Vibes",cursive;font-size:13.5px;
    display:flex;align-items:center;justify-content:center;padding-top:2px}
  .ribbon-left{left:20px}
  .ribbon-right{left:1096px}

  .headline{position:absolute;z-index:2;left:22px;top:298px;font-weight:200;font-size:23px;line-height:28px;color:#2a2a2a;white-space:nowrap}
  .headline .script{font-family:"Great Vibes",cursive;font-size:36px;color:#111;font-weight:400;margin-right:2px}

  .section{position:absolute;font-size:8.8px;line-height:11.3px;white-space:nowrap}
  .section h2{font-size:9.5px;font-weight:700;line-height:12px}
  .item b{font-weight:700}
  .item b::before{content:"";display:inline-block;width:3px;height:3px;background:var(--red);vertical-align:middle;margin:0 1px 2px 0}

  .adventure{left:306px;top:60px}
  .food{left:306px;top:150px}
  .spa{left:390px;top:240px}
  .spa .l{display:block}
  .water{left:622px;top:161px}
  .driving{left:622px;top:274px}

  .visit{position:absolute;left:971px;top:328px;width:229px;height:34px;background:var(--grey-band);
    font-size:9px;line-height:11px;padding:5px 6px;white-space:nowrap}
  .visit b{font-weight:700}
</style>
</head>
<body>
<main class="spread">
  <div class="photo photo-cooking" role="img" aria-label="Photo of a couple in aprons at a cooking class making fresh pasta"></div>
  <div class="photo photo-car" role="img" aria-label="Photo of a red supercar wheel and door on a grey road"></div>

  <div class="circle circle-spa" role="img" aria-label="Photo of a woman receiving a relaxing facial massage"></div>
  <div class="circle circle-sky" role="img" aria-label="Photo of a tandem skydiving pair in the sky"></div>
  <div class="circle circle-kayak" role="img" aria-label="Photo of an orange kayak paddle dipping into turquoise water"></div>

  <div class="ribbon ribbon-left">our experiences</div>
  <div class="ribbon ribbon-right">our experiences</div>

  <h1 class="headline"><span class="script">Explore</span> our most<br>popular experiences</h1>

  <section class="section adventure">
    <h2>Adventure</h2>
    <p class="item"><b>Skydiving:</b> Feel the rush of freefalling from thousands of feet<br>with an expert by your side.</p>
    <p class="item"><b>Bungee Jumping:</b> Leap off breathtaking heights and feel the<br>thrill of a lifetime.</p>
    <p class="item"><b>Scuba Diving:</b> Dive deep into crystal-clear waters and<br>explore the beauty beneath the surface.</p>
  </section>

  <section class="section food">
    <h2>Food &amp; Drink</h2>
    <p class="item"><b>Cooking Classes:</b> Master the art of gourmet cooking with<br>expert chefs.</p>
    <p class="item"><b>Wine Tasting:</b> Savor the finest wines and learn about<br>winemaking from local vintners.</p>
    <p class="item"><b>Street Food Tours:</b> Discover culinary delights with a guided tour<br>of local hidden gems.</p>
  </section>

  <section class="section spa">
    <h2>Relaxation &amp; Spa</h2>
    <p class="item">
      <span class="l" style="margin-left:14px"><b>Spa Day Packages:</b> Indulge in half and</span>
      <span class="l" style="margin-left:23px">full-day relaxation experiences for</span>
      <span class="l" style="margin-left:31px">individuals and couples</span>
    </p>
    <p class="item">
      <span class="l" style="margin-left:36px"><b>Wellness Retreats:</b> Reconnect with</span>
      <span class="l" style="margin-left:39px">yourself in peaceful surroundings</span>
      <span class="l" style="margin-left:40px">with yoga, meditation, and</span>
      <span class="l" style="margin-left:40px">wellness therapies.</span>
    </p>
    <p class="item">
      <span class="l" style="margin-left:40px"><b>Massages:</b> Discover a state of</span>
      <span class="l" style="margin-left:39px">relaxation and bliss at a choice of</span>
      <span class="l" style="margin-left:37px">days spas across the USA.</span>
    </p>
  </section>

  <section class="section water">
    <h2>Water Activities</h2>
    <p class="item"><b>Canoe and Kayaking:</b><br>Paddle through scenic rivers and lakes in<br>a peaceful or adventurous exploration.</p>
    <p class="item"><b>Marine Encounter:</b> Get up close with<br>marine life, from dolphins to sharks, in<br>unforgettable encounters.</p>
    <p class="item"><b>Boat Cruises:</b> Relax and enjoy scenic<br>views on luxurious or casual boat cruises.</p>
  </section>

  <section class="section driving">
    <h2>Driving &amp; Racing</h2>
    <p class="item"><b>Supercar Experiences:</b> Get behind the<br>wheel of high-performance supercars and<br>experience the thrill of speed.</p>
    <p class="item"><b>StockPro Experiences:</b> Drive like a pro and<br>feel the excitement of stock car racing.</p>
    <p class="item"><b>Rally Driving:</b> Navigate off-road tracks and<br>get a taste of professional rally driving.</p>
  </section>

  <p class="visit">Visit <b>JoyCrates.com</b> for a full list of experiences<br>and more detailed descriptions</p>
</main>
</body>
</html>
```